Rivers of Parting - CD cover indie music

This is my 4th and final album. I am sharing my story of trials, pain and persistence that led me here, like a sound track to a short film.
I would like a design that communicates both a painful phase of life, yet tranquility and beauty found as life winds down. Can be illustrated or photograph.
On front design should have title 'Rivers of Parting' and artist name.
I will need to add credits and song list.
I am thinking a booklet will be added with lyrics and a few photos and plan to work with this artist. Thank you

Target Market(s)

Folk, easy listening, story telling

Industry/Entity Type

Indie music - independent

Font styles to use
Sans Serif
Other font styles liked:
• I like also verdana font.

Requirements
Nice to have
• a contrast of colors to emotions may work well. There is a portuguese word ‘saudade’ that expresses sadness, but longing also.
Should not have
• No bright red. Not busy. No images of people or animals.

```html
<!DOCTYPE html>
<html lang="en">
<head>
<meta charset="UTF-8">
<title>Rivers of Parting – Album Cover</title>
<link rel="stylesheet" href="https://fonts.googleapis.com/css2?family=Questrial&display=swap">
<style>
  :root {
    --page-bg: #ffffff;
    --night-navy: #1a2350;
    --deep-navy: #131a3d;
    --storm-blue: #3a4275;
    --sun-gold: #e9a93a;
    --amber: #b87a22;
    --sun-glow: #fff3c8;
    --title-gold: #f6d383;
    --artist-grey: #c8cbd8;
  }
  * { margin: 0; padding: 0; box-sizing: border-box; }
  html, body {
    width: 960px;
    height: 1200px;
    overflow: hidden;
    background: var(--page-bg);
  }
  .canvas {
    position: relative;
    width: 960px;
    height: 1200px;
  }
  .album-cover {
    position: absolute;
    left: 40px;
    top: 160px;
    width: 880px;
    height: 880px;
    overflow: hidden;
  }
  .cover-artwork {
    position: absolute;
    inset: 0;
    background:
      radial-gradient(circle at 28% 11%, var(--sun-glow) 0, rgba(255,243,200,0.6) 5%, rgba(255,243,200,0) 14%),
      radial-gradient(ellipse 55% 45% at 82% 22%, rgba(233,169,58,0.95) 0, rgba(184,122,34,0.7) 45%, rgba(184,122,34,0) 100%),
      linear-gradient(215deg, var(--amber) 0%, rgba(58,66,117,0.9) 38%, var(--night-navy) 62%, var(--deep-navy) 100%);
  }
  .album-title {
    position: absolute;
    left: 70px;
    top: 634px;
    font-family: "Questrial", "Verdana", sans-serif;
    font-size: 84px;
    line-height: 0.9;
    font-weight: 400;
    letter-spacing: 0.5px;
    color: var(--title-gold);
    text-transform: uppercase;
  }
  .artist-name {
    position: absolute;
    left: 280px;
    top: 822px;
    font-family: "Questrial", "Verdana", sans-serif;
    font-size: 17px;
    letter-spacing: 6px;
    color: var(--artist-grey);
    text-transform: uppercase;
  }
</style>
</head>
<body>
  <main class="canvas">
    <section class="album-cover">
      <div class="cover-artwork" role="img" aria-label="Dramatic sky of dark blue storm clouds with golden sunlight breaking through and light rays streaming diagonally down"></div>
      <h1 class="album-title">Rivers of<br>Parting</h1>
      <p class="artist-name">Artist-Arstistname</p>
    </section>
  </main>
</body>
</html>
```